Bright Ridge Coatings

Hi
I'm looking for a unique and eye-catching design for my business card that reflects the identity of my business. We specialize in residential, commercial, insurance, real state, heritage,and body corporate painting services and I want the card to make a memorable impression on potential clients.

Key elements to include are:
- Our logo (attached)
- Contact information: my name is darian volkema but my short name is dar, im a director of this business, number: 0457893014, email: info@brightridgecoatings.com.au
Website: www.brightridgecoatings.com.au
Social media: facebook, instagram.

I'm open to creative ideas and unconventional formats, but it's important that the design maintains a professional look.

I'd like to see some initial concepts within the few days, and I'm willing to discuss any ideas you have.

Looking forward to seeing your creativity at work!

I prefer the colours pretty much the same as my logo, but i would be happy see if my logo match with other colours.
Thanks very much

Best regards,
Dar

Our target market consists of residential exterior and interior painting, basically we do all commercial jobs, bod corporate , heritage

Residential and commercial painting

All my information as provided!! Im not sure if you guys have access to my logo through with all the format in my account??

Serif

• My business card should be double sided,
• Its nice to have all my information in front and the rest at the back, like what we we do like residential , interior exterior and as i mentioned

```html
<!DOCTYPE html>
<html lang="en">
<head>
<meta charset="utf-8">
<title>Bright Ridge Coatings – Business Card</title>
<link rel="stylesheet" href="https://fonts.googleapis.com/css2?family=Roboto+Condensed:wght@400;700&display=swap">
<style>
  :root {
    --stage: #222222;
    --card-dark: #1e1e23;
    --brand-red: #b3302c;
    --brand-red-deep: #a32925;
    --brand-blue: #3d5c93;
    --brand-green: #3f6b45;
    --text-light: #ffffff;
    --text-soft: #d8d8dc;
  }
  * { box-sizing: border-box; margin: 0; padding: 0; }
  html, body { width: 1200px; height: 780px; overflow: hidden; }
  body {
    background: var(--stage);
    font-family: "Roboto Condensed", Arial, sans-serif;
    position: relative;
  }
  .card {
    position: absolute;
    width: 540px;
    height: 330px;
    top: 225px;
    overflow: hidden;
    box-shadow: 0 14px 34px rgba(0,0,0,.55);
  }

  /* Front */
  .card-front { left: 30px; background: var(--card-dark); }
  .brand-lockup {
    position: absolute; left: 150px; top: 38px;
    display: flex; align-items: center; gap: 10px;
  }
  .brand-square { width: 22px; height: 22px; background: var(--brand-green); }
  .brand-name {
    font-weight: 700; font-size: 21px; letter-spacing: 2px;
    color: var(--brand-green); text-transform: uppercase; white-space: nowrap;
  }
  .name-block {
    position: absolute; left: 0; top: 96px;
    padding-left: 26px;
  }
  .name-bar {
    position: absolute; left: 0; top: 4px;
    width: 12px; height: 32px; background: var(--brand-red);
  }
  .person-name {
    font-weight: 700; font-size: 30px; line-height: 1.1;
    color: var(--brand-blue); white-space: nowrap;
  }
  .person-short { color: var(--brand-red); }
  .person-role { font-size: 14px; color: var(--text-soft); margin-top: 2px; }
  .contact-list {
    position: absolute; left: 26px; top: 172px;
    list-style: none; display: grid; gap: 6px;
    font-size: 14px; color: var(--text-light);
  }
  .contact-list li { display: flex; align-items: center; gap: 9px; white-space: nowrap; }
  .contact-icon { width: 13px; height: 13px; flex: none; }
  .band-red {
    position: absolute; left: 0; bottom: 26px;
    width: 300px; height: 30px; background: var(--brand-red);
    clip-path: polygon(0 0, 100% 0, 88% 100%, 0 100%);
  }
  .band-blue {
    position: absolute; right: 0; bottom: 0;
    width: 260px; height: 30px; background: var(--brand-blue);
    clip-path: polygon(8% 0, 100% 0, 100% 100%, 0 100%);
    display: flex; align-items: center; gap: 10px;
    padding-left: 48px;
    color: var(--text-light); font-size: 17px; white-space: nowrap;
  }
  .social-dot {
    width: 17px; height: 17px; border-radius: 50%;
    background: var(--text-light); flex: none;
  }

  /* Back */
  .card-back { left: 630px; background: var(--brand-red); }
  .back-texture {
    position: absolute; inset: 0;
    background: linear-gradient(135deg, var(--brand-red) 0%, var(--brand-red-deep) 100%);
  }
  .back-brand {
    position: absolute; right: 44px; top: 150px;
    display: flex; align-items: center; gap: 6px;
    color: var(--text-light);
    font-weight: 700; font-size: 11px; letter-spacing: 1px; text-transform: uppercase;
    white-space: nowrap;
  }
  .back-brand-square { width: 10px; height: 10px; background: var(--text-light); }
  .specialize-title {
    position: absolute; left: 226px; bottom: 60px;
    font-weight: 700; font-size: 17px; color: var(--text-light);
    text-transform: uppercase; white-space: nowrap;
  }
  .service-list {
    position: absolute; left: 22px; bottom: 32px;
    font-size: 13px; color: var(--text-light); white-space: nowrap;
  }
  .service-list .sep { margin: 0 3px; }
</style>
</head>
<body>

<section class="card card-front" aria-label="Business card front">
  <div class="brand-lockup">
    <span class="brand-square"></span>
    <span class="brand-name">Bright Ridge Coatings</span>
  </div>

  <div class="name-block">
    <span class="name-bar"></span>
    <h1 class="person-name">Darian Volkema <span class="person-short">(Dar)</span></h1>
    <p class="person-role">Director</p>
  </div>

  <ul class="contact-list">
    <li>
      <svg class="contact-icon" viewBox="0 0 16 16" aria-hidden="true"><path fill="#b3302c" d="M3.6 1.5l2.3 2.6-1.3 1.7c.9 2 2.6 3.7 4.6 4.6l1.7-1.3 2.6 2.3-1.3 2.3C7 13.5 2.5 9 1.3 2.8z"/></svg>
      045 789 3014
    </li>
    <li>
      <svg class="contact-icon" viewBox="0 0 16 16" aria-hidden="true"><rect x="1" y="3" width="14" height="10" rx="1.5" fill="#3f6b45"/><path d="M1.5 4l6.5 5 6.5-5" stroke="#1e1e23" stroke-width="1.3" fill="none"/></svg>
      info@brightridgecoatings.com.au
    </li>
    <li>
      <svg class="contact-icon" viewBox="0 0 16 16" aria-hidden="true"><circle cx="8" cy="8" r="7" fill="#3d5c93"/><path d="M1 8h14M8 1c2.5 2.5 2.5 11.5 0 14M8 1c-2.5 2.5-2.5 11.5 0 14" stroke="#1e1e23" stroke-width="1" fill="none"/></svg>
      www.brightridgecoatings.com.au
    </li>
  </ul>

  <div class="band-red"></div>
  <div class="band-blue">
    <span>Follow us</span>
    <span class="social-dot" role="img" aria-label="Social profile link"></span>
    <span class="social-dot" role="img" aria-label="Social profile link"></span>
  </div>
</section>

<section class="card card-back" aria-label="Business card back">
  <div class="back-texture" role="img" aria-label="Tone-on-tone repeating brand mark pattern across the red card"></div>
  <div class="back-brand">
    <span class="back-brand-square"></span>
    <span>Bright Ridge Coatings</span>
  </div>
  <h2 class="specialize-title">We Specialize</h2>
  <p class="service-list">
    Residential<span class="sep">●</span>Commercial<span class="sep">●</span>Insurance<span class="sep">●</span>Real state<span class="sep">●</span>Heritage<span class="sep">●</span>Body corporate painting services
  </p>
</section>

</body>
</html>
```